Ruvo Decor

There is a sample provided with the arabic text of the business card. please copy paste the same text and the same Logo (The two triangles) Just try to incorproate the Brown background attached (you are free to change the colors) Id like the colors to be mainly shades of black and red.

```html
<!DOCTYPE html>
<html lang="ar">
<head>
<meta charset="utf-8">
<title>Ruvo Decor – Business Card</title>
<link href="https://fonts.googleapis.com/css2?family=Tajawal:wght@400;500&family=Teko:wght@500&family=Roboto:wght@500&display=swap" rel="stylesheet">
<style>
  :root{
    --bg:#232323;
    --card:#181818;
    --ink:#f2f2f2;
    --red:#d40000;
    --crimson:#c8183f;
    --crimson-dark:#9c1a30;
    --grey:#3c3c3c;
  }
  *{margin:0;padding:0;box-sizing:border-box}
  html,body{width:1200px;height:1138px;overflow:hidden;background:var(--bg)}
  .card{position:absolute;left:276px;width:620px;height:375px;background:var(--card);border-radius:14px;overflow:hidden;box-shadow:0 6px 14px rgba(0,0,0,.45)}
  .card--front{top:186px}
  .card--back{top:608px}

  .decor-field{position:absolute;left:0;top:16px;width:262px;height:328px;
    background:linear-gradient(135deg,#3a3a3a 0%,#2a1618 55%,#3a1216 100%);opacity:.8}
  .credentials{position:absolute;right:92px;top:36px;list-style:none;direction:rtl;
    font-family:'Tajawal',sans-serif;font-size:21px;color:var(--ink);line-height:35px}
  .credentials li{position:relative;white-space:nowrap}
  .credentials li::before{content:"";position:absolute;right:-38px;top:10px;width:14px;height:14px;background:var(--red)}
  .band{position:absolute;left:0;bottom:0;width:100%;height:14px;background:var(--red)}

  .name-lettering{position:absolute;left:36px;top:40px;width:212px;height:70px;
    background:linear-gradient(90deg,#2b2b2b,#3a2225);border-radius:4px}
  .details{position:absolute;left:36px;top:160px;width:216px;direction:rtl;text-align:right;
    font-family:'Tajawal',sans-serif;font-size:20px;line-height:34.5px;color:var(--ink);white-space:nowrap}
  .phone{position:absolute;left:36px;top:310px;display:flex;align-items:center;gap:16px;
    font-family:'Roboto',sans-serif;font-weight:500;font-size:20px;color:var(--ink)}
  .phone svg{width:26px;height:26px}
  .brand-panel{position:absolute;left:0;top:0;width:620px;height:375px}
  .brand-name{position:absolute;left:390px;width:180px;top:236px;text-align:center;
    font-family:'Teko',sans-serif;font-weight:500;font-size:46px;letter-spacing:1px;color:#fff}
</style>
</head>
<body>

<section class="card card--front">
  <div class="decor-field" role="img" aria-label="Large faint brand mark decoration in grey and dark red"></div>
  <ul class="credentials">
    <li>ماجســـتير هندسة ديكور</li>
    <li>دبلوم عاي فن تشـــكيلي</li>
    <li>أكاديمية الفنون (ليون)</li>
    <li>استشارات هندسية - فنية</li>
    <li>ماجســـتير هندسة ديكور</li>
    <li>دبلوم عاي فن تشـــكيلي</li>
    <li>أكاديمية الفنون (ليون)</li>
    <li>استشارات هندسية - فنية</li>
  </ul>
  <div class="band"></div>
</section>

<section class="card card--back">
  <svg class="brand-panel" viewBox="0 0 620 375" aria-hidden="true">
    <defs>
      <linearGradient id="panelRed" x1="0" y1="0" x2="1" y2="1">
        <stop offset="0" stop-color="#a8223a"/>
        <stop offset=".5" stop-color="#c8183f"/>
        <stop offset="1" stop-color="#b01a36"/>
      </linearGradient>
    </defs>
    <path d="M370 0 C300 90 300 290 370 375 L620 375 L620 0 Z" fill="#e9e9e9"/>
    <path d="M378 0 C310 90 310 290 378 375 L620 375 L620 0 Z" fill="url(#panelRed)"/>
  </svg>
  <div class="brand-name">RUVO DECOR</div>

  <div class="name-lettering" role="img" aria-label="Hand-lettered name: المهندس / سالم يوسف النعيمي، أستاذ جامعي"></div>
  <div class="details">
    ماجســـتير هندسة ديكور<br>
    دبلوم عاي فن تشـــكيلي<br>
    أكاديمية الفنون (ليون)<br>
    استشارات هندسية -فنية
  </div>
  <div class="phone">
    <svg viewBox="0 0 26 26" aria-hidden="true">
      <circle cx="13" cy="13" r="11.5" fill="none" stroke="#d40000" stroke-width="1.6"/>
      <path d="M9 8.5c-1 1-1 3 1 5.5s4.5 3.5 5.8 2.5l1.2-1.2-2-1.8-1.1.8c-.8-.3-2.4-2-2.7-2.8l.8-1.1-1.8-2z" fill="#d40000"/>
    </svg>
    <span>30012045/66100288</span>
  </div>
</section>

</body>
</html>
```